Business Card for Makeup Artist

I need a business card designed for my makeup and hair artistry business which is primarily events and weddings focused. The card needs to be sleek, simple, stylish and appealing to women. I would prefer a white background but open to suggestions also. I also love the marble background look. I have attached some example pics. It needs to be a double sided card with logo and/or design on one side and contact details in the centre of the card on the other side. NO LOGO ON BACK. Examples attached.

Target Market(s)

Females age 14-55

Industry/Entity Type

Business

Contact Information for Business Card

Nora Vint
Principal Makeup Artist
P: 0413 925 214
E: nora@lumirabeauty.com.au
W: www.lumirabeauty.com.au

Requirements
Should not have
• No yellow, green, red or blue in the design.

```html
<!DOCTYPE html>
<html lang="en">
<head>
<meta charset="utf-8">
<title>Lumira Makeup Artistry – Business Card</title>
<link rel="stylesheet" href="https://fonts.googleapis.com/css2?family=Questrial&display=swap">
<style>
  :root {
    --page: #2b2a2a;
    --marble-light: #f7f7f7;
    --marble-mid: #e6e6e6;
    --marble-vein: #cfcfcf;
    --ink: #7a7a7a;
    --ink-soft: #8c8c8c;
    --gold: #b39660;
  }
  * { box-sizing: border-box; margin: 0; padding: 0; }
  html, body {
    width: 1200px;
    height: 1200px;
    overflow: hidden;
    background: var(--page);
    font-family: "Questrial", sans-serif;
  }
  .canvas {
    position: relative;
    width: 1200px;
    height: 1200px;
  }
  .card {
    position: absolute;
    left: 220px;
    width: 760px;
    height: 434px;
    overflow: hidden;
    box-shadow: 0 8px 24px rgba(0, 0, 0, 0.45);
  }
  .card--front { top: 130px; }
  .card--back { top: 636px; }
  .card__marble {
    position: absolute;
    inset: 0;
    background:
      radial-gradient(ellipse 60% 40% at 20% 30%, var(--marble-mid), transparent 70%),
      radial-gradient(ellipse 50% 35% at 80% 70%, var(--marble-vein), transparent 70%),
      radial-gradient(ellipse 40% 30% at 65% 20%, var(--marble-mid), transparent 70%),
      linear-gradient(135deg, var(--marble-light), #efefef 50%, var(--marble-light));
  }
  .card__frame {
    position: absolute;
    border: 3px solid var(--gold);
    left: 50%;
    top: 50%;
    transform: translate(-50%, -50%);
    display: flex;
    flex-direction: column;
    justify-content: center;
  }
  .card--front .card__frame {
    width: 320px;
    height: 170px;
    align-items: center;
  }
  .brand__name {
    font-size: 64px;
    line-height: 1;
    color: var(--ink);
    letter-spacing: 1px;
  }
  .brand__tagline {
    margin-top: 10px;
    font-size: 20px;
    letter-spacing: 1.5px;
    color: var(--ink-soft);
  }
  .card--back .card__frame {
    width: 330px;
    height: 236px;
    padding: 0 18px;
    align-items: flex-start;
  }
  .contact__name {
    font-size: 46px;
    line-height: 1.05;
    color: var(--ink);
  }
  .contact__role {
    margin-top: 6px;
    font-size: 14.5px;
    letter-spacing: 1.3px;
    color: var(--ink-soft);
  }
  .contact__details {
    margin-top: 26px;
    list-style: none;
    font-size: 14.5px;
    line-height: 1.35;
    letter-spacing: 0.6px;
    color: var(--ink);
  }
  .contact__phone { padding-left: 76px; }
</style>
</head>
<body>
  <main class="canvas">
    <section class="card card--front" aria-label="Business card front">
      <div class="card__marble" role="img" aria-label="White marble background with soft grey veining"></div>
      <div class="card__frame">
        <div class="brand__name">Lumira</div>
        <div class="brand__tagline">MAKEUP ARTISTRY</div>
      </div>
    </section>

    <section class="card card--back" aria-label="Business card back">
      <div class="card__marble" role="img" aria-label="White marble background with soft grey veining"></div>
      <div class="card__frame">
        <h1 class="contact__name">Nora Vint</h1>
        <p class="contact__role">PRINCIPAL MAKEUP ARTIST</p>
        <ul class="contact__details">
          <li class="contact__phone">0413 925 214</li>
          <li>nora@lumirabeauty.com.au</li>
          <li>www.lumirabeauty.com.au</li>
        </ul>
      </div>
    </section>
  </main>
</body>
</html>
```